New Business Card Design Project

Looking for a modern business card design for an import distribution business for industrial technical products. The winning design will translate modern, sophistication, technical, professional and sustainable.

Target Market(s)

Technical customers

Industry/Entity Type

Business

Contact Information for Business Card

Dean Harlow
Sales Manager
M: 0471 625 183
P: 1300 872 619
dean@volkarsystems.com.au
4/18 Galloway Crest Road
Kelvin Park NSW 2159
www.volkarsystems.com.au

Font styles to use
Sans Serif

Colors
ec1f27
606060
000000
fbfbfb

Requirements
Must have
• My Logo which is the Volkar Systems logo attached
Nice to have
• Eurostile Bold font

```html
<!DOCTYPE html>
<html lang="en">
<head>
<meta charset="utf-8">
<title>Volkar Systems – Business Card</title>
<link rel="stylesheet" href="https://fonts.googleapis.com/css2?family=Montserrat:wght@400;600;700&family=Saira:wght@600;700&display=swap">
<style>
  :root {
    --red: #ec1f27;
    --red-deep: #c8262a;
    --grey: #606060;
    --ink: #000000;
    --paper: #fbfbfb;
    --backdrop: #262626;
  }
  * { box-sizing: border-box; margin: 0; padding: 0; }
  html, body { width: 1200px; height: 783px; overflow: hidden; }
  body {
    background: var(--backdrop);
    font-family: "Montserrat", sans-serif;
    position: relative;
  }
  .card {
    position: absolute;
    width: 520px;
    height: 297px;
    top: 243px;
    border-radius: 3px;
    overflow: hidden;
    box-shadow: 0 14px 30px rgba(0,0,0,.45);
  }
  .card--back {
    left: 50px;
    background: linear-gradient(135deg, var(--red) 0%, var(--red-deep) 100%);
  }
  .card--back .brand-square {
    position: absolute;
    right: 52px;
    bottom: 44px;
    width: 56px;
    height: 56px;
    background: #bdbdbd;
  }
  .card--front {
    left: 630px;
    background: var(--paper);
    color: var(--grey);
  }
  .brand {
    position: absolute;
    left: 28px;
    top: 36px;
    display: flex;
    align-items: center;
    gap: 12px;
  }
  .brand__square {
    width: 26px;
    height: 26px;
    background: var(--red);
  }
  .brand__name {
    font-family: "Montserrat", sans-serif;
    font-weight: 700;
    font-size: 25px;
    letter-spacing: 1px;
    color: var(--red);
    text-transform: uppercase;
  }
  .stripe {
    position: absolute;
    top: 108px;
    left: 0;
    width: 100%;
    height: 12px;
  }
  .stripe__red {
    position: absolute;
    left: 0; top: 0;
    width: 458px; height: 12px;
    background: var(--red);
  }
  .stripe__grey {
    position: absolute;
    right: 0; top: 0;
    width: 52px; height: 12px;
    background: var(--grey);
  }
  .person {
    position: absolute;
    left: 28px;
    top: 136px;
  }
  .person__name {
    font-family: "Saira", sans-serif;
    font-weight: 700;
    font-size: 21px;
    color: var(--red);
    text-transform: uppercase;
    line-height: 1.1;
  }
  .person__role {
    font-family: "Saira", sans-serif;
    font-weight: 600;
    font-size: 14px;
    color: var(--grey);
    text-transform: uppercase;
    margin-bottom: 4px;
  }
  .person__address {
    font-style: normal;
    font-size: 13px;
    line-height: 1.4;
  }
  .contact {
    position: absolute;
    right: 26px;
    bottom: 20px;
    text-align: right;
    font-size: 13px;
    line-height: 1.45;
  }
  .contact__label {
    color: var(--red);
    font-weight: 700;
  }
</style>
</head>
<body>
  <section class="card card--back" aria-label="Card back">
    <div class="brand-square"></div>
  </section>

  <section class="card card--front" aria-label="Card front">
    <div class="brand">
      <div class="brand__square"></div>
      <div class="brand__name">Volkar Systems</div>
    </div>

    <div class="stripe">
      <div class="stripe__red"></div>
      <div class="stripe__grey"></div>
    </div>

    <div class="person">
      <div class="person__name">Dean Harlow</div>
      <div class="person__role">Sales Manager</div>
      <address class="person__address">
        4/18 Galloway Crest Road<br>
        Kelvin Park NSW 2159
      </address>
    </div>

    <div class="contact">
      <div><span class="contact__label">Phone :</span> 1300 872 619</div>
      <div><span class="contact__label">Mobile :</span> 0471 625 183</div>
      <div>dean@volkarsystems.com.au</div>
      <div>www.volkarsystems.com.au</div>
    </div>
  </section>
</body>
</html>
```